Lantern Crest Gathering Day 2021

I am looking to create a flyer for a one day prayer retreat our church is organizing. This flyer will be posted on social media, websites, mobile apps, and will also be printed so it can be mailed to people.

I am looking for something professional, with good use of our logo and band colors (logo colors).

I am counting on the designer's skill, creativity, art and knowledge of media communication to produce a flyer that will effectively and quickly convey the message we are trying to spread.

CONTENT OF THE FLYER:
Event title: Lantern Crest Gathering Day
Date: Tuesday July 2nd, 2021
Time: 11:00AM - 7:00PM
Brindlewick Hotel, 4817 Fennimore Street, Portland, Maine 04102 (Room: Thistlemoor)
Event Key words to highlight what the event is about: Prayer, Fasting, Worship, Prophecy, Revival.
Key phrases:
A one day prayer retreat.
Jesus Chris is Lord

Contact info:
www.velunto.org
Phone: 207 555 0143
Email: contact@quillbrookfold.org

```html
<!DOCTYPE html>
<html lang="en">
<head>
<meta charset="utf-8">
<title>Lantern Crest Gathering Day 2021</title>
<link href="https://fonts.googleapis.com/css2?family=Montserrat:wght@400;600;800&family=Oswald:wght@400;600&family=Cinzel:wght@500&display=swap" rel="stylesheet">
<style>
  :root{
    --page:#8e8e8e;
    --navy:#1b2a48;
    --navy-deep:#16223c;
    --blue:#2c4a72;
    --teal:#24404a;
    --orange:#f0a02a;
    --white:#ffffff;
  }
  *{margin:0;padding:0;box-sizing:border-box}
  html,body{width:1200px;height:845px;overflow:hidden;background:var(--page)}
  .flyer{position:absolute;left:324px;top:22px;width:552px;height:800px;overflow:hidden;
    font-family:'Montserrat',sans-serif;color:var(--white);box-shadow:0 8px 30px rgba(0,0,0,.35)}
  .backdrop{position:absolute;inset:0;
    background:radial-gradient(ellipse at 80% 20%,#325a86 0%,transparent 55%),
               radial-gradient(ellipse at 60% 65%,#2e4f6e 0%,transparent 50%),
               linear-gradient(160deg,var(--teal) 0%,var(--blue) 60%,#2a4a78 100%)}
  .orange-band{position:absolute;left:33px;top:0;width:201px;height:800px;
    background:linear-gradient(180deg,#d08536 0%,#c57a33 50%,#b9692a 100%)}
  .title-block{position:absolute;left:0;top:80px;width:348px;height:230px;background:var(--navy)}
  .title{position:absolute;left:33px;top:16px;width:310px;font-weight:800;font-size:31px;line-height:42px;
    letter-spacing:-.3px;white-space:nowrap}
  .title .accent{color:var(--orange)}
  .tagline{position:absolute;left:31px;top:152px;font-size:13.5px;letter-spacing:3.2px;font-weight:400;white-space:nowrap}
  .motto{position:absolute;left:0;top:182px;width:348px;height:29px;background:var(--orange);
    color:var(--navy-deep);font-weight:800;font-size:22px;line-height:29px;padding-left:31px;letter-spacing:.5px;white-space:nowrap}
  .motto .thin{font-weight:400}
  .brand{position:absolute;left:395px;top:95px;width:200px;height:50px;transform-origin:0 0;
    transform:translate(0,205px) rotate(-90deg);font-family:'Cinzel',serif;font-size:46px;line-height:50px;
    letter-spacing:2px;color:var(--white);white-space:nowrap}
  .brand-dot{position:absolute;left:440px;top:290px;width:14px;height:14px;border-radius:50%;background:var(--orange)}
  .keywords{position:absolute;left:258px;top:372px;width:280px;display:grid;grid-template-columns:150px 130px;row-gap:21px;list-style:none}
  .keyword{display:flex;align-items:center;gap:12px;font-family:'Oswald',sans-serif;font-size:19px;letter-spacing:.3px}
  .keyword svg{width:34px;height:34px;flex:none}
  .day{position:absolute;left:258px;top:556px;font-weight:800;font-size:45px;letter-spacing:-.5px;line-height:48px;white-space:nowrap}
  .date{position:absolute;left:258px;top:604px;font-family:'Cinzel',serif;font-size:44px;line-height:48px;color:var(--orange);white-space:nowrap}
  .year{position:absolute;left:500px;top:646px;transform-origin:0 0;transform:rotate(-90deg);
    font-size:32px;font-weight:400;color:var(--orange);line-height:32px;letter-spacing:2px;white-space:nowrap}
  .time{position:absolute;left:258px;top:667px;width:270px;height:52px;background:var(--orange);color:var(--navy-deep);
    font-family:'Oswald',sans-serif;font-weight:600;font-size:31px;line-height:52px;text-align:center;white-space:nowrap;letter-spacing:-.3px}
  .venue{position:absolute;left:258px;top:728px;width:292px;font-size:15.5px;line-height:21px}
  .call{position:absolute;left:23px;top:655px;width:214px;height:51px;background:var(--navy);color:var(--orange);
    font-family:'Oswald',sans-serif;font-weight:600;font-size:34px;line-height:51px;text-align:center;white-space:nowrap}
  .phone{position:absolute;left:33px;top:708px;width:201px;text-align:center;font-family:'Oswald',sans-serif;
    font-weight:600;font-size:34px;line-height:44px;white-space:nowrap}
  .contact{position:absolute;left:47px;font-family:'Cinzel',serif;font-size:9.5px;display:flex;align-items:center;gap:7px;white-space:nowrap}
  .contact svg{width:10px;height:10px}
  .contact.email{top:754px}
  .contact.web{top:771px}
</style>
</head>
<body>
<main class="flyer">
  <div class="backdrop" role="img" aria-label="Soft blue-toned photograph of a person in worship"></div>
  <div class="orange-band"></div>

  <section class="title-block">
    <h1 class="title"><span class="accent">LANTERN CREST</span><br>GATHERING<br>DAY</h1>
    <p class="tagline">A ONE DAY PRAYER RETREAT</p>
    <p class="motto">JESUS CHRIS <span class="thin">IS</span> LORD</p>
  </section>

  <span class="brand-dot"></span>
  <div class="brand">VELUNTO</div>

  <ul class="keywords">
    <li class="keyword"><svg viewBox="0 0 34 34"><circle cx="17" cy="17" r="15.5" fill="none" stroke="var(--orange)" stroke-width="1.5"/><path d="M17 8c1 4 6 6 5 12a5 5 0 0 1-10 0c0-3 2-4 2-6 1 2 2 3 3 3 0-3-1-6 0-9z" fill="var(--orange)"/></svg>PRAYER</li>
    <li class="keyword"><svg viewBox="0 0 34 34"><circle cx="17" cy="17" r="15.5" fill="none" stroke="var(--orange)" stroke-width="1.5"/><path d="M17 8c1 4 6 6 5 12a5 5 0 0 1-10 0c0-3 2-4 2-6 1 2 2 3 3 3 0-3-1-6 0-9z" fill="var(--orange)"/></svg>FASTING</li>
    <li class="keyword"><svg viewBox="0 0 34 34"><circle cx="17" cy="17" r="15.5" fill="none" stroke="var(--orange)" stroke-width="1.5"/><path d="M17 8c1 4 6 6 5 12a5 5 0 0 1-10 0c0-3 2-4 2-6 1 2 2 3 3 3 0-3-1-6 0-9z" fill="var(--orange)"/></svg>WORSHIP</li>
    <li class="keyword"><svg viewBox="0 0 34 34"><circle cx="17" cy="17" r="15.5" fill="none" stroke="var(--orange)" stroke-width="1.5"/><path d="M17 8c1 4 6 6 5 12a5 5 0 0 1-10 0c0-3 2-4 2-6 1 2 2 3 3 3 0-3-1-6 0-9z" fill="var(--orange)"/></svg>PROPHECY</li>
    <li class="keyword"><svg viewBox="0 0 34 34"><circle cx="17" cy="17" r="15.5" fill="none" stroke="var(--orange)" stroke-width="1.5"/><path d="M17 8c1 4 6 6 5 12a5 5 0 0 1-10 0c0-3 2-4 2-6 1 2 2 3 3 3 0-3-1-6 0-9z" fill="var(--orange)"/></svg>REVIVAL</li>
  </ul>

  <p class="day">TUESDAY</p>
  <p class="date">July 2nd</p>
  <p class="year">2021</p>
  <p class="time">11:00AM - 7:00PM</p>
  <p class="venue">Brindlewick Hotel, 4817 Fennimore Street, Portland, Maine 04102</p>

  <p class="call">CALL US NOW</p>
  <p class="phone">207 555 0143</p>
  <p class="contact email"><svg viewBox="0 0 10 10"><circle cx="5" cy="5" r="4.5" fill="none" stroke="#fff" stroke-width=".8"/><rect x="2.6" y="3.4" width="4.8" height="3.2" fill="none" stroke="#fff" stroke-width=".7"/></svg>contact@quillbrookfold.org</p>
  <p class="contact web"><svg viewBox="0 0 10 10"><circle cx="5" cy="5" r="4.5" fill="none" stroke="#fff" stroke-width=".8"/><ellipse cx="5" cy="5" rx="1.8" ry="4.3" fill="none" stroke="#fff" stroke-width=".6"/><line x1=".6" y1="5" x2="9.4" y2="5" stroke="#fff" stroke-width=".6"/></svg>www.velunto.org</p>
</main>
</body>
</html>
```